I need the following on my business card:
- Name: Dana Whitcomb
- License # 0M93216
- Title: Producer
- Phone: (555) 017-3904
- Email: Dana@CorbelInsuranceServices.com

- Company: Corbel Insurance Services
- Address: 27408 Larkmoor Ave Suite 610, Sherman Oaks, CA 90217
- Website: www.CorbelInsuranceServices.com

Also add our slogan on the card: "Where Trust Meets Coverage"

```html
<!DOCTYPE html>
<html lang="en">
<head>
<meta charset="utf-8">
<title>Corbel Insurance Services – Business Card</title>
<link rel="stylesheet" href="https://fonts.googleapis.com/css2?family=Arimo:wght@400;700&family=Source+Sans+3:wght@600&display=swap">
<style>
  :root {
    --board: #253673;
    --navy: #253673;
    --green: #1f9a48;
    --paper: #f7fbfd;
    --stage: #c9c9c9;
    --label: #ffffff;
  }
  * { box-sizing: border-box; margin: 0; padding: 0; }
  html, body { width: 1034px; height: 1200px; overflow: hidden; }
  body {
    background: var(--board);
    position: relative;
    font-family: "Arimo", Arial, sans-serif;
    color: var(--navy);
  }
  .board-label {
    position: absolute;
    font-family: "Source Sans 3", "Myriad Pro", sans-serif;
    font-weight: 600;
    font-size: 40px;
    color: var(--label);
    line-height: 1;
  }
  .board-label--front { left: 96px; top: 116px; }
  .board-label--back { left: 852px; top: 116px; }
  .board-label--showcase { left: 106px; top: 456px; }

  .card {
    position: absolute;
    width: 482px;
    height: 275px;
    background: var(--paper);
    overflow: hidden;
  }
  .card--front { left: 25px; top: 157px; }
  .card--back { left: 528px; top: 157px; }

  .showcase {
    position: absolute;
    left: 25px; top: 511px;
    width: 985px; height: 655px;
    background: var(--stage);
  }
  .showcase .card {
    left: 190px; top: 155px;
    transform: scale(1.25);
    transform-origin: top left;
    box-shadow: 0 6px 18px rgba(0,0,0,.18);
  }

  /* Front */
  .card__name {
    position: absolute; right: 40px; top: 30px;
    font-size: 31px; font-weight: 700; letter-spacing: .3px;
  }
  .card__title {
    position: absolute; right: 44px; top: 68px;
    font-size: 13px; color: var(--green); letter-spacing: 2.6px;
  }
  .card__license {
    position: absolute; right: 47px; top: 85px;
    width: 160px; height: 21px;
    background: var(--navy); color: #fff;
    border-radius: 10px 0 0 0;
    font-size: 13.5px; font-weight: 700; letter-spacing: .4px;
    text-align: right; padding-right: 6px; line-height: 21px;
  }
  .contact {
    position: absolute; right: 64px;
    font-size: 14.5px; display: flex; align-items: center; gap: 10px;
  }
  .contact--phone { top: 161px; }
  .contact--email { top: 192px; }
  .contact svg { width: 18px; height: 18px; fill: var(--navy); }
  .card__slogan {
    position: absolute; right: 64px; top: 230px;
    font-size: 14.5px; font-weight: 700;
  }
  .card__accent {
    position: absolute; left: 430px; top: 152px;
    width: 9px; height: 104px; background: var(--green);
  }

  /* Back */
  .brand {
    position: absolute; left: 0; right: 0; top: 108px;
    display: flex; justify-content: center; align-items: center; gap: 8px;
  }
  .brand__dot { width: 12px; height: 12px; background: var(--green); }
  .brand__name {
    font-size: 19px; font-weight: 700; color: var(--navy); letter-spacing: 1.5px;
  }
  .brand-slogan {
    position: absolute; left: 138px; top: 181px;
    width: 212px; height: 24px; border-radius: 12px;
    background: var(--navy); color: #fff;
    font-size: 11.5px; text-align: center; line-height: 24px;
  }
  .brand-address, .brand-web {
    position: absolute; left: 0; right: 0; text-align: center;
    font-size: 12.5px;
  }
  .brand-address { top: 228px; }
  .brand-web { top: 249px; }
</style>
</head>
<body>
  <div class="board-label board-label--front">front</div>
  <div class="board-label board-label--back">Back</div>

  <section class="card card--front">
    <div class="card__name">Dana Whitcomb</div>
    <div class="card__title">PRODUCER</div>
    <div class="card__license">License # 0M93216</div>
    <div class="contact contact--phone">(555) 017-3904
      <svg viewBox="0 0 24 24" aria-hidden="true"><path d="M6.6 10.8c1.4 2.8 3.8 5.1 6.6 6.6l2.2-2.2c.3-.3.7-.4 1-.2 1.1.4 2.3.6 3.6.6.6 0 1 .4 1 1V20c0 .6-.4 1-1 1C10.6 21 3 13.4 3 4c0-.6.4-1 1-1h3.5c.6 0 1 .4 1 1 0 1.3.2 2.5.6 3.6.1.3 0 .7-.2 1z"/></svg>
    </div>
    <div class="contact contact--email">Dana@CorbelInsuranceServices.com
      <svg viewBox="0 0 24 24" aria-hidden="true"><path d="M2 5h20v14H2z M2 6l10 7 10-7v2l-10 7L2 8z" fill-rule="evenodd"/></svg>
    </div>
    <div class="card__slogan">"Where Trust Meets Coverage"</div>
    <div class="card__accent"></div>
  </section>

  <section class="card card--back">
    <div class="brand"><span class="brand__dot"></span><span class="brand__name">CORBEL INSURANCE SERVICES</span></div>
    <div class="brand-slogan">"Where Trust Meets Coverage"</div>
    <div class="brand-address">27408 Larkmoor Ave Suite 610 Sherman Oaks, CA 90217</div>
    <div class="brand-web">www.CorbelInsuranceServices.com</div>
  </section>

  <div class="board-label board-label--showcase">mock-up</div>
  <div class="showcase">
    <section class="card card--front">
      <div class="card__name">Dana Whitcomb</div>
      <div class="card__title">PRODUCER</div>
      <div class="card__license">License # 0M93216</div>
      <div class="contact contact--phone">(555) 017-3904
        <svg viewBox="0 0 24 24" aria-hidden="true"><path d="M6.6 10.8c1.4 2.8 3.8 5.1 6.6 6.6l2.2-2.2c.3-.3.7-.4 1-.2 1.1.4 2.3.6 3.6.6.6 0 1 .4 1 1V20c0 .6-.4 1-1 1C10.6 21 3 13.4 3 4c0-.6.4-1 1-1h3.5c.6 0 1 .4 1 1 0 1.3.2 2.5.6 3.6.1.3 0 .7-.2 1z"/></svg>
      </div>
      <div class="contact contact--email">Dana@CorbelInsuranceServices.com
        <svg viewBox="0 0 24 24" aria-hidden="true"><path d="M2 5h20v14H2z M2 6l10 7 10-7v2l-10 7L2 8z" fill-rule="evenodd"/></svg>
      </div>
      <div class="card__slogan">"Where Trust Meets Coverage"</div>
      <div class="card__accent"></div>
    </section>
  </div>
</body>
</html>
```